Local Self Storage Company needs a namecard

We need to have a namecard designed out based on the attached logo.

to have a very simple yet modern namecard design to show to others that we are a company that provides self storage and event logistics

Design to be in the format of Ai, PSD and Jpeg when selected

Target Market(s)

customers who are moving house or office
companies that need to have bigger spaces for storage
both for short term or long term

Industry/Entity Type

Self Storage

Requirements
Must have
• The front of the namecard to just have the logo and tag line

The back of the namecard to input the information as:
XX (Name)
XXX (Title)
XX(Hp)
41 Pembrook Crescent, Kavrel Industrial Building,
#03-11 Singapore 519264

```html
<!DOCTYPE html>
<html lang="en">
<head>
<meta charset="utf-8">
<title>KeepVault Namecard</title>
<link rel="stylesheet" href="https://fonts.googleapis.com/css2?family=Michroma&family=Source+Sans+3:wght@400;600&display=swap">
<style>
  :root {
    --page-bg: #ece9e4;
    --card-front-top: #ffffff;
    --card-front-bottom: #d9dadc;
    --card-back: #6b6c70;
    --brand-blue: #1f4fa0;
    --brand-green: #6cb33f;
    --rule-grey: #808184;
    --tagline-grey: #5e5f63;
    --tagline-faint: #8b8c90;
    --mark-faint: #7d7e82;
    --text-light: #ffffff;
  }
  * { margin: 0; padding: 0; box-sizing: border-box; }
  html, body {
    width: 1200px;
    height: 1159px;
    overflow: hidden;
    background: var(--page-bg);
  }
  .canvas {
    position: relative;
    width: 1200px;
    height: 1159px;
    font-family: "Source Sans 3", "Myriad Pro", Arial, sans-serif;
  }
  .card {
    position: absolute;
    width: 707px;
    height: 408px;
    overflow: hidden;
  }
  /* Front */
  .card-front {
    left: 133px;
    top: 149px;
    background: linear-gradient(to bottom, var(--card-front-top) 0%, var(--card-front-top) 35%, var(--card-front-bottom) 100%);
  }
  .brand-dot {
    position: absolute;
    left: 100px;
    top: 104px;
    width: 176px;
    height: 176px;
    border-radius: 50%;
    background: var(--brand-green);
  }
  .brand-name {
    position: absolute;
    left: 296px;
    top: 168px;
    font-family: "Source Sans 3", Arial, sans-serif;
    font-weight: 600;
    font-size: 46px;
    line-height: 1;
    letter-spacing: 0.5px;
    color: var(--brand-blue);
  }
  .front-tagline {
    position: absolute;
    left: 320px;
    top: 218px;
    font-family: "Michroma", "Eurostile", sans-serif;
    font-size: 11px;
    letter-spacing: 4.3px;
    color: var(--tagline-grey);
    white-space: nowrap;
  }
  .front-rule {
    position: absolute;
    left: 88px;
    top: 345px;
    width: 540px;
    height: 3px;
    background: var(--rule-grey);
  }
  /* Back */
  .card-back {
    left: 368px;
    top: 608px;
    background: var(--card-back);
    color: var(--text-light);
  }
  .back-tagline {
    position: absolute;
    left: 76px;
    top: 50px;
    font-family: "Michroma", "Eurostile", sans-serif;
    font-size: 19px;
    letter-spacing: 11.2px;
    color: var(--tagline-faint);
    white-space: nowrap;
  }
  .back-mark {
    position: absolute;
    left: 441px;
    top: 155px;
    width: 194px;
    height: 194px;
    border-radius: 50%;
    background: var(--mark-faint);
  }
  .contact {
    position: absolute;
    left: 53px;
    top: 222px;
  }
  .contact-name {
    font-size: 28px;
    font-weight: 400;
    line-height: 1.1;
  }
  .contact-title {
    font-size: 22px;
    line-height: 1.2;
    margin-top: 2px;
  }
  .contact-address {
    font-style: normal;
    font-size: 17px;
    line-height: 22px;
    margin-top: 16px;
  }
  .website {
    position: absolute;
    left: 232px;
    top: 368px;
    font-size: 21px;
  }
</style>
</head>
<body>
<main class="canvas">
  <section class="card card-front" aria-label="Namecard front">
    <span class="brand-dot" aria-hidden="true"></span>
    <h1 class="brand-name">KEEPVAULT</h1>
    <p class="front-tagline">YOUR STORAGE SOLUTION</p>
    <div class="front-rule"></div>
  </section>

  <section class="card card-back" aria-label="Namecard back">
    <p class="back-tagline">YOUR STORAGE SOLUTION</p>
    <span class="back-mark" aria-hidden="true"></span>
    <div class="contact">
      <p class="contact-name">Marcus Tan</p>
      <p class="contact-title">Co-founder</p>
      <address class="contact-address">41 Pembrook Crescent, Kavrel Industrial Building,<br>#03-11 Singapore 519264</address>
    </div>
    <p class="website">www.keepvault.com</p>
  </section>
</main>
</body>
</html>
```